Flyer Design Project

Just needing a sleek, modern brochure design for my Paint Contracting business. It's a one sided leaflet (99mm X 210mm)

Brennard Finish Coatings
"Over 25 years experience"
"We set the standard for quality and service"

Call for a free estimate:
Dorian Velsher 0498153620
Dorianvelsher0@quillmail.com
http://brennardfinishcoatings.webnest.com.au/

All Painting services offered:
Interior, exterior, pressure washing, staing, roof restoration, residential, commercial and body corporate

Target Market(s)

Home owners

Industry/Entity Type

Business

```html
<!DOCTYPE html>
<html lang="en">
<head>
<meta charset="utf-8">
<title>Brennard Finish Coatings – Flyer</title>
<link rel="stylesheet" href="https://fonts.googleapis.com/css2?family=Coustard:wght@400;900&family=Mulish:wght@600;700;800&display=swap">
<style>
  :root {
    --page-bg: #eceeed;
    --flyer-white: #ffffff;
    --header-blue: #3a3389;
    --ink-blue: #2f2a86;
    --cream: #fdf0d9;
    --alert-red: #d6281c;
    --ink-black: #1d1d1d;
    --dot-red: #e0262b;
    --dot-orange: #ef7d22;
    --dot-purple: #a04a8c;
    --dot-yellow: #f4e313;
    --dot-cyan: #1ba9e1;
    --dot-green: #1e9a4a;
    --display: "Coustard", "Cooper Black", Georgia, serif;
    --body: "Mulish", "Century Gothic", Arial, sans-serif;
  }
  * { margin: 0; padding: 0; box-sizing: border-box; }
  html, body { width: 1200px; height: 2345px; overflow: hidden; background: var(--page-bg); }
  .canvas { position: relative; width: 1200px; height: 2345px; }

  .flyer {
    position: absolute; left: 68px; top: 59px; width: 1040px; height: 2208px;
    background: var(--flyer-white); overflow: hidden;
    box-shadow: 0 4px 22px rgba(0,0,0,.18);
  }
  .flyer > * { position: absolute; }

  .header-band { left: 0; top: 0; width: 100%; height: 318px; background: var(--header-blue); }
  .brand-title {
    left: 0; top: 0; width: 100%; height: 318px;
    display: flex; flex-direction: column; justify-content: center; align-items: center;
    font-family: var(--display); font-weight: 900; font-size: 90px; line-height: 134px;
    color: #fff; text-align: center; white-space: nowrap;
    text-shadow: 3px 3px 0 #1a1640, -2px -2px 0 #1a1640, 2px -2px 0 #1a1640, -2px 2px 0 #1a1640, 4px 5px 3px rgba(0,0,0,.5);
  }

  .cream-panel { left: 0; top: 318px; width: 100%; height: 1251px; background: var(--cream); }
  .swatch-fan {
    left: 0; top: 318px; width: 100%; height: 400px;
    background:
      linear-gradient(to bottom, rgba(253,240,217,0) 45%, var(--cream) 100%),
      linear-gradient(100deg, #4fa6c9 0%, #8fc46b 18%, #d8d84a 34%, #f2c33a 48%, #f39a37 62%, #ea5b3a 78%, #d93a3a 100%);
  }

  .outlined {
    color: var(--ink-blue); font-family: var(--display); font-weight: 900; text-align: center; width: 100%; left: 0;
    white-space: nowrap;
    text-shadow: 2px 2px 0 #fff, -2px -2px 0 #fff, 2px -2px 0 #fff, -2px 2px 0 #fff, 3px 4px 4px rgba(0,0,0,.35);
  }
  .experience { top: 362px; font-size: 50px; line-height: 70px; }
  .experience .big { font-size: 68px; }
  .standard { top: 478px; font-size: 64px; line-height: 84px; }
  .customers {
    top: 687px; left: 0; width: 100%; text-align: center; white-space: nowrap;
    font-family: var(--display); font-weight: 900; font-size: 42px; color: var(--alert-red); line-height: 60px;
  }
  .customers .big { font-size: 54px; }
  .services-heading {
    top: 797px; left: 0; width: 100%; text-align: center; white-space: nowrap;
    font-family: var(--display); font-weight: 900; font-size: 50px; color: var(--ink-blue); line-height: 70px;
  }

  .painter-photo {
    left: 772px; top: 1040px; width: 250px; height: 1120px; z-index: 1;
    background: linear-gradient(to bottom, #4a4f6e 0%, #6b6e86 9%, #e6e8ec 16%, #f3f4f6 75%, #9da0a8 100%);
    border-radius: 110px 110px 18px 18px;
  }

  .service-list { left: 80px; top: 918px; list-style: none; z-index: 2; }
  .service-list li {
    position: relative; padding-left: 63px; white-space: nowrap;
    font-family: var(--body); font-weight: 700; font-size: 41px; line-height: 61px; color: var(--ink-blue);
  }
  .service-list li::before {
    content: ""; position: absolute; left: 3px; top: 20px; width: 22px; height: 22px; border-radius: 50%; background: var(--dot);
  }
  .service-list li.no-dot::before { display: none; }

  .offer-note {
    left: 88px; top: 1388px; z-index: 2; white-space: nowrap;
    font-family: var(--body); font-weight: 800; font-size: 27px; line-height: 40px; color: var(--ink-black);
  }
  .offer-note .conditions { margin-top: 8px; }

  .brand-square { left: 125px; top: 1592px; width: 100px; height: 100px; background: var(--dot-green); z-index: 2; }
  .brand-name {
    left: 84px; top: 1714px; z-index: 2; white-space: nowrap;
    font-family: var(--body); font-weight: 800; font-size: 31px; line-height: 40px; color: var(--ink-black);
  }

  .cans-photo {
    left: 520px; top: 1705px; width: 320px; height: 280px; z-index: 3;
    background: radial-gradient(ellipse at 50% 45%, #e9eaec 0%, #c7c9cd 60%, #f4f4f5 100%);
    border-radius: 24px;
  }

  .contact-line { left: 88px; z-index: 2; white-space: nowrap; color: var(--ink-black); font-family: var(--body); font-weight: 800; }
  .estimate { top: 1808px; font-size: 28px; line-height: 46px; }
  .phone {
    top: 1924px; display: flex; align-items: center; gap: 12px;
    font-family: var(--display); font-weight: 900; font-size: 46px; color: var(--alert-red); line-height: 60px;
  }
  .phone svg { width: 40px; height: 40px; flex: none; }
  .email { top: 2022px; font-size: 28px; line-height: 40px; }
  .web { top: 2092px; font-size: 28px; line-height: 40px; }
</style>
</head>
<body>
<div class="canvas">
  <main class="flyer">
    <div class="header-band"></div>
    <h1 class="brand-title"><span>Brennard Finish</span><span>Coatings</span></h1>

    <div class="cream-panel"></div>
    <div class="swatch-fan" role="img" aria-label="Fanned paint colour swatch cards in a rainbow of colours"></div>

    <p class="outlined experience">Over <span class="big">25</span> years experience</p>
    <p class="outlined standard">We set the standard<br>for quality and service</p>
    <p class="customers">Over <span class="big">1500</span> Satisfied Customers</p>
    <h2 class="services-heading">All Painting services offered:</h2>

    <div class="painter-photo" role="img" aria-label="Photo of a painter in white overalls and cap, seen from behind, rolling paint with a long-handled roller"></div>

    <ul class="service-list">
      <li style="--dot: var(--dot-red)">Interior</li>
      <li style="--dot: var(--dot-orange)">Exterior</li>
      <li style="--dot: var(--dot-purple)">Pressure washing</li>
      <li style="--dot: var(--dot-yellow)">Staing</li>
      <li style="--dot: var(--dot-cyan)">Roof restoration</li>
      <li style="--dot: var(--dot-green)">Residential,commercial</li>
      <li class="no-dot">and body corporate</li>
    </ul>

    <div class="offer-note">
      <p>3 Bedroom Home Interior starting at $3000<br>Financing Available</p>
      <p class="conditions">(conditions apply, excludes GST)</p>
    </div>

    <div class="brand-square"></div>
    <p class="brand-name">Brennard Finish Coatings</p>

    <div class="cans-photo" role="img" aria-label="Photo of open paint tins in red, yellow, blue and green"></div>

    <p class="contact-line estimate">Call for a free estimate:<br>Dorian Velsher</p>
    <p class="contact-line phone">
      <svg viewBox="0 0 42 42" aria-hidden="true">
        <circle cx="21" cy="21" r="19" fill="none" stroke="#d6281c" stroke-width="2.5"/>
        <path d="M14 11c2-1 3 0 4 2l1 3c0 1-1 2-2 3 1 3 3 5 6 6 1-1 2-2 3-2l3 1c2 1 3 2 2 4-1 2-3 3-5 3-7-1-13-7-14-14 0-3 1-5 2-6z" fill="none" stroke="#d6281c" stroke-width="2.2"/>
      </svg>
      0498153620
    </p>
    <p class="contact-line email">Dorianvelsher0@quillmail.com</p>
    <p class="contact-line web">brennardfinishcoatings.webnest.com.au</p>
  </main>
</div>
</body>
</html>
```